BKT Business Card

Business card design for a handyman company. Want to portray a professional image and stay away from the "Mom & Pops" image that is normally associated with handyman companies.

```html
<!DOCTYPE html>
<html lang="en">
<head>
<meta charset="utf-8">
<title>BKT Business Card</title>
<link href="https://fonts.googleapis.com/css2?family=Source+Sans+3:wght@400;600;700&family=Arimo:wght@400&display=swap" rel="stylesheet">
<style>
  :root {
    --backdrop: #ecebe8;
    --card: #ffffff;
    --navy: #1b2447;
    --ink: #2a2a2a;
    --ghost: #e3e8ec;
    --rule: #555a66;
  }
  * { box-sizing: border-box; margin: 0; padding: 0; }
  html, body {
    width: 1200px; height: 563px; overflow: hidden;
    background: var(--backdrop);
    font-family: "Source Sans 3", Arial, sans-serif;
    color: var(--ink);
  }
  .stage { position: relative; width: 1200px; height: 563px; }
  .card {
    position: absolute; top: 150px;
    width: 460px; height: 263px;
    background: var(--card);
    border-radius: 24px;
    box-shadow: 0 6px 18px rgba(0,0,0,0.18);
    overflow: hidden;
  }
  .card--front { left: 95px; }
  .card--back { left: 645px; }

  .brand-name {
    position: absolute;
    font-weight: 700;
    color: var(--navy);
    letter-spacing: 1px;
    line-height: 1;
  }
  .card--front .brand-name { left: 28px; top: 26px; font-size: 54px; }
  .card--back .brand-name { left: 34px; top: 98px; font-size: 58px; }

  .brand-ghost {
    position: absolute; right: 34px; bottom: 42px;
    font-weight: 700; font-size: 50px; letter-spacing: 1px;
    color: var(--ghost); line-height: 1;
  }

  .holder { position: absolute; right: 34px; top: 110px; text-align: right; }
  .holder-name { font-weight: 700; font-size: 18px; color: var(--navy); }
  .holder-title { font-size: 13px; color: var(--ink); margin-top: 2px; }

  .contact-list {
    position: absolute; left: 44px; top: 170px;
    list-style: none; font-size: 15px; line-height: 22px;
  }
  .contact-list li { display: flex; align-items: center; gap: 4px; }
  .contact-list svg { width: 12px; height: 12px; fill: var(--navy); flex: none; }
  .contact-list .address { font-size: 13px; padding-left: 1px; }

  .service-lead {
    position: absolute; left: 212px; top: 40px;
    font-family: "Arimo", Arial, sans-serif; font-size: 14px;
  }
  .service-divider {
    position: absolute; left: 224px; top: 72px;
    width: 1px; height: 110px; background: var(--rule);
  }
  .service-list {
    position: absolute; left: 234px; top: 66px;
    list-style: none;
    font-family: "Arimo", Arial, sans-serif; font-size: 14px; line-height: 24px;
  }
  .website {
    position: absolute; left: 0; right: 0; bottom: 34px; text-align: center;
    font-family: "Arimo", Arial, sans-serif; font-size: 14px; letter-spacing: 1.4px;
  }
</style>
</head>
<body>
<main class="stage">
  <section class="card card--front" aria-label="Card front">
    <div class="brand-name">BKT</div>
    <div class="brand-ghost" aria-hidden="true">BKT</div>
    <div class="holder">
      <p class="holder-name">Your Name</p>
      <p class="holder-title">Title</p>
    </div>
    <ul class="contact-list">
      <li>
        <svg viewBox="0 0 24 24" aria-hidden="true"><path d="M6.6 10.8a15 15 0 0 0 6.6 6.6l2.2-2.2a1 1 0 0 1 1-.25 11 11 0 0 0 3.6.6 1 1 0 0 1 1 1V20a1 1 0 0 1-1 1A17 17 0 0 1 3 4a1 1 0 0 1 1-1h3.5a1 1 0 0 1 1 1 11 11 0 0 0 .6 3.6 1 1 0 0 1-.25 1z"/></svg>
        555-240-1170
      </li>
      <li>
        <svg viewBox="0 0 24 24" aria-hidden="true"><circle cx="12" cy="7" r="5"/><path d="M2 22c0-5.5 4.5-9 10-9s10 3.5 10 9z"/></svg>
        555-260-3381
      </li>
      <li>
        <svg viewBox="0 0 24 24" aria-hidden="true"><path d="M2 5h20v14H2z M3 6l9 7 9-7" stroke="#fff" stroke-width="1.5"/></svg>
        info@BKTHomeServices.com
      </li>
      <li class="address">410 N Elm St., Fairview, KS 66000</li>
    </ul>
  </section>

  <section class="card card--back" aria-label="Card back">
    <div class="brand-name">BKT</div>
    <p class="service-lead">Residential &amp; Commercial Services</p>
    <div class="service-divider"></div>
    <ul class="service-list">
      <li>Potential Verbage</li>
      <li>Home Repairs</li>
      <li>Handyman Services</li>
      <li>DrainCleaning</li>
      <li>Carpet Cleaning</li>
    </ul>
    <p class="website">www.bktHomeServices.com</p>
  </section>
</main>
</body>
</html>
```